Political sign design, fonts colors and layout

I am running for Town Council.

My message is done, and *a draft is attached* with the text we wish to use. It says "Elect Dana Velloway" etc. In Maroon and White. I am not a designer, but this is somewhat close to what we are looking for.

I need help with colors and fonts, layout, spacing, and general cleanup.

I'm attaching the town high school logo:

- "B" for Brockmere: with black and white outlines on the fonts
- we want to incorporate the black and white on the fonts
- for the entire text, parts of the text, or best would be a mix

This is for signs printed and placed all over my town.

We need two versions

1. square, 4' by 4' version
2. 36" by 24" version

The smaller version will drop the three bullet pointed text, but otherwise can be identical.

The sign can only use 3 printed colors (due to printing costs.)

1. maroon,
2. white,
3. black.

The maroon should match the maroon from the high school logo attached, which I believe I did in the draft.

We also like the white border around the outside, like in the "scoreboard" design attached.

Thanks for your attention, wish me luck.

Dana

Target Market(s)

SIgns, Political market

Industry/Entity Type

Political

Font styles to use
Sans Serif
Other font styles liked:
• Arial Black, Sans Serif Bold

Requirements
Must have
• maroon background, white font.
• - black borders around fonts where appropriate
• - great spacing
• - great typeface usage
• - clean and crisp political sign, visible while driving.
• - my name "Dana Velloway" much larger like the draft, or the appropriate additional size
• - two versions, one square, and one 36" / 24"
Nice to have
• - nice borders
• - dress it up a bit, using italics and bold fonts, without making it flashy or busy.
Should not have
• Must be easily readable from a car, except for "Paid for by Friends of Dana Velloway" which can be tiny.
• Colors are noted in the description, the "Brockmere Maroon" as the background, white font, and some use of black.

```html
<!DOCTYPE html>
<html lang="en">
<head>
<meta charset="utf-8">
<title>Elect Dana Velloway – Yard Sign</title>
<link rel="stylesheet" href="https://fonts.googleapis.com/css2?family=Raleway:wght@400;800&display=swap">
<style>
  :root {
    --maroon: #761c30;
    --white: #ffffff;
    --black: #000000;
    --sign-size: 1200px;
    --outline:
      3px 0 0 var(--black), -3px 0 0 var(--black),
      0 3px 0 var(--black), 0 -3px 0 var(--black),
      2px 2px 0 var(--black), -2px -2px 0 var(--black),
      2px -2px 0 var(--black), -2px 2px 0 var(--black);
    --outline-thin:
      2px 0 0 var(--black), -2px 0 0 var(--black),
      0 2px 0 var(--black), 0 -2px 0 var(--black),
      1.5px 1.5px 0 var(--black), -1.5px -1.5px 0 var(--black),
      1.5px -1.5px 0 var(--black), -1.5px 1.5px 0 var(--black);
  }
  * { margin: 0; padding: 0; box-sizing: border-box; }
  html, body {
    width: var(--sign-size);
    height: var(--sign-size);
    overflow: hidden;
    background: var(--white);
  }
  .sign {
    position: relative;
    width: var(--sign-size);
    height: var(--sign-size);
    background: var(--white);
    border: 2px solid var(--maroon);
    font-family: "Raleway", Arial, sans-serif;
    overflow: hidden;
  }
  .panel {
    position: absolute;
    left: 18px;
    right: 18px;
    background: var(--maroon);
  }
  .panel--top { top: 14px; height: 444px; }
  .panel--bottom { top: 592px; height: 592px; }

  .rule {
    position: absolute;
    height: 3px;
    background: var(--white);
  }
  .rule--elect-left  { top: 409px; left: 18px;  width: 392px; }
  .rule--elect-right { top: 409px; left: 788px; width: 394px; }
  .rule--vote-left   { top: 983px; left: 18px;  width: 136px; }
  .rule--vote-right  { top: 983px; left: 1046px; width: 136px; }

  .line {
    position: absolute;
    left: 0;
    right: 0;
    text-align: center;
    line-height: 1;
    white-space: nowrap;
    font-weight: 800;
    color: var(--white);
    text-shadow: var(--outline);
  }
  .slogan    { top: 155px; font-size: 114px; letter-spacing: 0; }
  .elect     { top: 357px; font-size: 100px; letter-spacing: -1px; }
  .candidate { top: 470px; font-size: 120px; color: var(--maroon); letter-spacing: -2px; }
  .tagline   { top: 686px; font-size: 96px; letter-spacing: -1px; }
  .website   { top: 797px; font-size: 64px; text-shadow: var(--outline-thin); }
  .vote-date { top: 943px; font-size: 86px; letter-spacing: -1px; }
  .disclaimer{ top: 1112px; font-size: 38px; font-weight: 400; text-shadow: none; }
</style>
</head>
<body>
  <main class="sign">
    <div class="panel panel--top"></div>
    <div class="panel panel--bottom"></div>

    <div class="rule rule--elect-left"></div>
    <div class="rule rule--elect-right"></div>
    <div class="rule rule--vote-left"></div>
    <div class="rule rule--vote-right"></div>

    <p class="line slogan">Take Back Our Town</p>
    <p class="line elect">ELECT</p>
    <h1 class="line candidate">DANA VELLOWAY</h1>
    <p class="line tagline">Fighting for Brockmere</p>
    <p class="line website">www.votedana.com</p>
    <p class="line vote-date">Vote Nov. 8th "Row A"</p>
    <p class="line disclaimer">Paid for by Friends of Dana</p>
  </main>
</body>
</html>
```